KORIN-NUT vegan protein

Hi
We need a vegan protein label and logo for our company
KORIN-NUT
We made a quick sketch in the type of way we want it But you can always make it better
Dont mind the logo we sketched please come up with something else
Left side of the label please the color of the taste So brown red vanille we need 3 designs for Chocolate, strawberry and vanilla
Backside: leave nutrition faces blank,
One square text with: Pea Protein derived and extracted from organic grean split peas. It is a great source of fiber (helps with digestion and less bloating), vitamines and minerals. Studies have shown that the intake of pea protein can reduce high blood pressure and that it can be used for prevention and controll of diabetes as it has minimal effect on blood glucose levels and insulin response.
One square with suggested use:
Add 1 or 2 scoops to a blender, shaker or glass with cold water or your favorite beverage (various amount of liquid to achieve your desired taste). Shake or mix well before consumption.
Distributed by:
BRAMOSK COMPANY BV
THE NETHERLANDS
Please make it look amazing elegant and premium elite looking
It will be made on a alu bag like a send In the pictures

```html
<!DOCTYPE html>
<html lang="en">
<head>
<meta charset="utf-8">
<title>KORIN-NUT Organic Vegan Protein – Chocolate Label</title>
<link rel="stylesheet" href="https://fonts.googleapis.com/css2?family=Montserrat:wght@700;800&family=Roboto+Condensed:wght@400&display=swap">
<style>
  :root {
    --backdrop: #58585b;
    --flavour-brown: #5e3714;
    --label-white: #ffffff;
    --ink-dark: #3a3a3c;
    --badge-dark: #6d6e71;
    --badge-light: #a7a9ac;
    --choc-deep: #4a2814;
    --choc-mid: #7b4a2a;
  }
  * { margin: 0; padding: 0; box-sizing: border-box; }
  html, body { width: 1200px; height: 922px; overflow: hidden; }
  body { background: var(--backdrop); position: relative; font-family: "Montserrat", sans-serif; }

  .label {
    position: absolute; left: 330px; top: 25px;
    width: 540px; height: 872px;
    background: var(--label-white);
    box-shadow: 0 6px 18px rgba(0,0,0,.35);
    overflow: hidden;
  }
  .flavour-band {
    position: absolute; left: 0; top: 0; width: 145px; height: 100%;
    background: var(--flavour-brown);
  }
  .band-brand {
    position: absolute; left: 81px; top: 430px;
    transform: translate(-50%, -50%) rotate(-90deg);
    white-space: nowrap;
    color: var(--label-white);
    font-weight: 800; font-size: 66px; letter-spacing: 1px; line-height: 1;
  }
  .band-brand sup { font-size: 22px; font-weight: 700; vertical-align: top; margin-left: 4px; }
  .flavour-photo {
    position: absolute; left: 18px; top: 730px; width: 110px; height: 110px;
    border-radius: 50%; border: 3px solid var(--label-white);
    background: radial-gradient(circle at 45% 40%, var(--choc-mid), var(--choc-deep) 70%);
    box-shadow: inset 0 0 0 3px var(--flavour-brown);
  }

  .front {
    position: absolute; left: 145px; top: 0; width: 395px; height: 100%;
    text-align: center;
  }
  .title-organic {
    position: absolute; left: 0; width: 100%; top: 170px;
    color: var(--flavour-brown); font-weight: 800; font-size: 57px; line-height: 1;
  }
  .title-product {
    position: absolute; left: 0; width: 100%; top: 230px;
    color: var(--flavour-brown); font-weight: 800; font-size: 30px; line-height: 1;
  }
  .brand-mark {
    position: absolute; left: 39px; top: 330px; width: 318px; height: 120px;
    display: flex; align-items: center; justify-content: center; gap: 14px;
  }
  .brand-mark .mark-square { width: 26px; height: 26px; background: var(--flavour-brown); }
  .brand-mark .mark-name {
    color: var(--flavour-brown); font-weight: 800; font-size: 46px; line-height: 1;
  }
  .claim-figure {
    position: absolute; left: 0; width: 100%; top: 490px;
    color: var(--ink-dark); font-weight: 800; font-size: 104px; line-height: 1; letter-spacing: 1px;
  }
  .claim-text {
    position: absolute; left: 0; width: 100%; top: 603px;
    color: var(--ink-dark); font-weight: 800; font-size: 35px; line-height: 1;
  }
  .badges {
    position: absolute; left: 18px; top: 680px; width: 360px; height: 80px;
  }
  .badge {
    position: absolute; width: 70px; height: 70px; border-radius: 50%;
    display: flex; flex-direction: column; align-items: center; justify-content: center;
    color: var(--label-white); font-family: "Roboto Condensed", sans-serif;
    font-size: 10px; line-height: 1.1; text-transform: uppercase;
  }
  .badge b { font-weight: 400; font-size: 15px; }
  .badge--dark { background: var(--badge-dark); }
  .badge--light { background: var(--badge-light); }
  .badge:nth-child(1) { left: 0; top: 0; }
  .badge:nth-child(2) { left: 69px; top: 10px; }
  .badge:nth-child(3) { left: 140px; top: 0; }
  .badge:nth-child(4) { left: 207px; top: 10px; }
  .badge:nth-child(5) { left: 278px; top: 0; }

  .net-weight {
    position: absolute; left: 94px; top: 801px; width: 194px; height: 38px;
    background: var(--flavour-brown); color: var(--label-white);
    border-radius: 20px 0 20px 0;
    font-weight: 700; font-size: 16px; line-height: 38px;
  }
</style>
</head>
<body>
  <div class="label">
    <div class="flavour-band">
      <div class="band-brand">KORIN-NUT<sup>®</sup></div>
      <div class="flavour-photo" role="img" aria-label="Chocolate pieces photo showing the chocolate flavour"></div>
    </div>

    <div class="front">
      <h1 class="title-organic">ORGANIC</h1>
      <h2 class="title-product">VEGAN PROTEIN</h2>

      <div class="brand-mark">
        <span class="mark-square"></span>
        <span class="mark-name">KORIN-NUT</span>
      </div>

      <div class="claim-figure">100%</div>
      <div class="claim-text">PLANT BASED</div>

      <div class="badges">
        <div class="badge badge--dark"><b>0</b>Sugare</div>
        <div class="badge badge--light"><b>7g</b>Organic</div>
        <div class="badge badge--dark"><b>21 g</b>Protein</div>
        <div class="badge badge--light"><b>GF</b></div>
        <div class="badge badge--dark">Super<br>Food<br>Vitamines</div>
      </div>

      <div class="net-weight">Net Wt. 700 g</div>
    </div>
  </div>
</body>
</html>
```